Corbin Lantern Lighting - Commercial & Residential Landscape Lighting

Landscape Lighting Services & Design: Create a website for our landscape lighting company. We would like the design to be tailored around this description:
Illuminate with Confidence. Designed with Precision. Installed with Care.
Locally and veteran-owned, we take pride in transforming outdoor spaces through innovative lighting solutions tailored to your vision. From landscape and holiday lighting to permanent installations, our effortless process and expert design deliver breathtaking results and lasting curb appeal. Backed by a lifetime warranty and quarterly service options, our commitment to quality and customer satisfaction is unwavering. Try before you buy and experience your home in a whole new light with our complimentary demo kit — see the stunning effects before you decide.
- Also, add in this information as well; Outdoor Lighting not only beautifies spaces but also significantly enhances safety by illuminating your home or business. Beautifully lit entrances deter potential intruders, making your home a safer place for your loved ones. we also offer quarterly service plans to ensure lighting equipment continues to operate & illuminate effectively throughout the year. Also mention we provide free estimates and we are offering a 10% discount to military, veterans, and first responders.

Target Market(s)

Luxury market

Industry/Entity Type

Landscape Lighting - Residential & Commercial Lighting Services

Coding

Coded - Design and coding required

Number of Pages Required

2 page

Colors
00AB8E
00BBA5
67D7C9
C6EFE9
E9F9F6
59FF00
82FF00
B8FF75
E3FFCB
F4FFEA
FFC000
F8CF3A
FAE287
FDF2CF
FEFAEE

Requirements
Must have
• a lead generation button where people can submit their information for us to reach out to them and schedule their free estimate, homepage, about page, contact page, products and services page, user friendly, easy to navigate, and it also must be engaging and eye popping, as well as appealing to the luxury market. Please use colors; verdent green, dark green, ivory, and sunny yellow. Also, include an about page that references our story; Derek is retired Army and he opened a fitness studio in 2017 with his wife Vanessa. He has installed low voltage lighting in every home he lived in and for his friends and family over the years and decided to open his own business because he is passionate about beautifying outdoor landscapes and highlighting a properties full potential, not only in the day but at night as well all while providing safety and security for his clients. Having a deep respect for nature and landscaping, he wants to provide the same care and quality to each of his clients as he has in the fitness industry for decades. He believes small businesses are the back bone of America and he's excited to provide a service that is all to often neglected in the design of a home.
Nice to have
• I would like to have a clear intent and purpose, engaging web design, clear call to action, optimized for search engines, mobile friendy design, security measures, credibility indicators

```html
<!DOCTYPE html>
<html lang="en">
<head>
<meta charset="utf-8">
<title>Corbin Lantern Lighting – Landscape Lighting</title>
<link href="https://fonts.googleapis.com/css2?family=Josefin+Sans:wght@400;600;700&family=Mulish:wght@400;600;700;800&family=Poppins:wght@600;700&display=swap" rel="stylesheet">
<style>
:root{
  --green:#1f8f70;
  --green-dark:#17755b;
  --gold:#f6a71c;
  --ink:#2b2b2b;
  --text:#4a4a4a;
  --white:#ffffff;
  --brick:#ececec;
  --footer:#161616;
}
*{margin:0;padding:0;box-sizing:border-box}
html,body{width:1200px;height:4549px;overflow:hidden}
body{position:relative;font-family:"Mulish",sans-serif;color:var(--text);background:var(--white)}
.abs{position:absolute}
.heading{font-family:"Josefin Sans",sans-serif;font-weight:400;color:var(--ink);font-size:38px;letter-spacing:1px;line-height:1}
.rule{position:absolute;height:4px;width:72px;background:var(--gold)}
.btn{position:absolute;background:var(--gold);color:#fff;font-weight:800;font-size:13px;display:flex;align-items:center;justify-content:center;gap:5px;text-transform:uppercase}
.btn .dot{width:11px;height:11px;border-radius:50%;background:#fff;display:inline-flex;align-items:center;justify-content:center}
.btn .dot::after{content:"";border-left:4px solid var(--gold);border-top:3px solid transparent;border-bottom:3px solid transparent;margin-left:1px}
.photo{position:absolute}

/* header */
.topline{left:0;top:0;width:1200px;height:4px;background:var(--green)}
.logo{left:110px;top:28px;display:flex;align-items:center;gap:10px;font-family:"Josefin Sans",sans-serif;font-weight:700;color:#b3202a;font-size:20px;line-height:1.05;width:180px}
.logo .mark{width:16px;height:16px;border-radius:50%;background:#b3202a;flex:none}
.nav{left:408px;top:40px;display:flex;gap:26px;font-size:14px;font-weight:600;color:#333}
.nav .active{color:var(--green);position:relative}
.nav .active::after{content:"";position:absolute;left:0;right:0;bottom:-8px;height:2px;background:var(--green)}
.call{left:865px;top:30px;display:flex;gap:12px;align-items:center}
.call .ico{width:36px;height:36px;border-radius:50%;background:var(--gold);display:flex;align-items:center;justify-content:center}
.call small{display:block;font-size:13px;color:#333}
.call strong{display:block;font-size:21px;color:var(--gold);font-weight:700;letter-spacing:.5px}

/* hero */
.hero{left:0;top:100px;width:1200px;height:668px;background:linear-gradient(180deg,#3a4a4c 0%,#2f3a33 35%,#4a3a26 60%,#3d4a25 85%,#2c3a1e 100%);overflow:hidden}
.hero h1{position:absolute;left:0;width:1200px;top:168px;text-align:center;color:#fff;font-family:"Josefin Sans",sans-serif;font-weight:400;font-size:43px;line-height:43px;letter-spacing:1.5px}
.hero p{position:absolute;left:300px;width:600px;top:258px;text-align:center;color:#fff;font-size:14px;line-height:25px}
.dots{position:absolute;left:570px;top:520px;display:flex;gap:3px}
.dots span{width:12px;height:12px;border-radius:50%;background:#fff}
.dots span:first-child{background:var(--gold)}
.hero svg{position:absolute;left:0;bottom:0}

/* about */
.frame{left:110px;top:943px;width:318px;height:337px;border:14px solid var(--green);border-top:none;border-right:none}
.frame-top{left:110px;top:943px;width:70px;height:14px;background:var(--green)}
.frame-right{left:414px;top:1237px;width:14px;height:43px;background:var(--green)}
.about-text{left:632px;top:925px;width:456px;font-size:13.4px;line-height:24px;text-align:justify;color:#444}

/* services */
.services{left:0;top:1580px;width:1200px;height:644px;background:var(--brick)}
.svc{position:absolute;top:198px;width:300px;text-align:center}
.svc .ring{width:296px;height:296px;border-radius:50%;background:var(--green);display:flex;align-items:center;justify-content:center;margin:0 auto;box-shadow:inset -6px -4px 0 #f3c35a}
.svc .pic{width:252px;height:252px;border-radius:50%}
.svc h3{font-size:20px;font-weight:600;color:#222;margin-top:22px}
.arrow{position:absolute}

/* offer */
.offer-box{left:571px;top:2323px;width:535px;height:325px;background:var(--green);color:#fff;padding:48px 0 0 63px;font-family:"Josefin Sans",sans-serif;font-size:32px;line-height:40px}
.offer-box .big{color:var(--gold);font-size:47px;font-weight:700;line-height:56px;margin:10px 0 6px}

/* blog */
.blog{left:0;top:3362px;width:1200px;height:700px;background:var(--brick)}
.card{position:absolute;top:203px;width:313px}
.card .pic{width:313px;height:180px}
.card .body{background:#fff;width:289px;height:210px;padding:20px 16px}
.card h4{font-size:20px;font-weight:800;color:#222}
.card .date{font-size:14px;color:var(--green);margin:8px 0 6px;display:flex;gap:5px;align-items:center}
.card p{font-size:13px;line-height:26px;color:#666}

/* footer */
.footer{left:0;top:4032px;width:1200px;height:517px;background:var(--footer);color:#fff}
.footer h5{position:absolute;top:178px;font-family:"Poppins",sans-serif;font-weight:700;font-size:24px}
.flist{position:absolute;top:240px;list-style:none;font-size:14px;line-height:26px}
.flist li{display:flex;gap:26px;align-items:center}
.flist li::before{content:"»";color:var(--gold);font-size:16px}
.contact-item{position:absolute;left:437px;display:flex;gap:22px;font-size:14px;line-height:26px}
.copy{position:absolute;left:0;width:1200px;top:4493px;text-align:center;font-size:13px;color:#fff}
</style>
</head>
<body>

<!-- Header -->
<div class="abs topline"></div>
<div class="abs logo"><span class="mark"></span>Corbin Lantern Lighting</div>
<nav class="abs nav"><span class="active">Home</span><span>About</span><span>Product</span><span>Services</span><span>Contact</span></nav>
<div class="abs call">
  <div class="ico"><svg width="16" height="16" viewBox="0 0 24 24"><path fill="#fff" d="M6.6 10.8a15 15 0 006.6 6.6l2.2-2.2c.3-.3.7-.4 1-.2 1.1.4 2.3.6 3.6.6.6 0 1 .4 1 1V20c0 .6-.4 1-1 1A17 17 0 013 4c0-.6.4-1 1-1h3.5c.6 0 1 .4 1 1 0 1.3.2 2.5.6 3.6.1.3 0 .7-.2 1z"/></svg></div>
  <div><small>Call us Today :</small><strong>+1 888 888 8888</strong></div>
</div>

<!-- Hero -->
<section class="abs hero" role="img" aria-label="Brick home with warm landscape lighting at dusk">
  <h1>DESIGNED WITH PRECISION.<br>INSTALLED WITH CARE.</h1>
  <p>Locally and veteran-owned, we take pride in transforming outdoor spaces through innovative lighting solutions tailored to your vision.</p>
  <div class="btn" style="left:478px;top:323px;width:244px;height:43px">Schedule a free estimate</div>
  <div class="dots"><span></span><span></span><span></span><span></span></div>
  <svg width="1200" height="90" viewBox="0 0 1200 90"><path d="M0 90 Q600 -30 1200 90Z" fill="var(--gold)"/><path d="M0 90 Q600 -10 1200 90Z" fill="#fff"/></svg>
</section>

<!-- About -->
<div class="abs frame"></div>
<div class="photo" style="left:177px;top:826px;width:320px;height:337px;background:linear-gradient(160deg,#2c3a30,#6a4a2a 55%,#2f3b22)" role="img" aria-label="Lit brick house exterior"></div>
<div class="photo" style="left:316px;top:973px;width:252px;height:264px;background:#fff;padding:4px"><div style="width:100%;height:100%;background:linear-gradient(135deg,#4d6470,#2b3a44)" role="img" aria-label="Portrait of Derek, the owner"></div></div>
<h2 class="abs heading" style="left:632px;top:848px">ABOUT DEREK</h2>
<div class="rule" style="left:632px;top:897px"></div>
<p class="abs about-text">Derek is retired Army and he opened a fitness studio in 2017 with his wife Vanessa. He has installed low voltage lighting in every home he lived in and for his friends and family over the years and decided to open his own business because he is passionate about beautifying outdoor landscapes and highlighting a properties full potential, not only in the day but at night as well all while providing safety and security for his clients. Having a deep respect for nature and landscaping, he wants to provide the same care and quality to each of his clients as he has in the fitness industry for decades. He believes small businesses are the back bone of America and he's excited to provide a service that is all to often neglected in the design of a home.</p>
<div class="btn" style="left:632px;top:1237px;width:151px;height:42px">Learn more <span class="dot"></span></div>
<div class="photo" style="left:0;top:1270px;width:1200px;height:310px;background:linear-gradient(180deg,#fff 0%,rgba(255,255,255,0) 30%),linear-gradient(180deg,#6a7466 20%,#4b5a3a 55%,#8a6a3a 80%,#3a4a22)" role="img" aria-label="Lit stone garden path lined with plants"></div>

<!-- Services -->
<section class="abs services">
  <h2 class="heading" style="position:absolute;left:0;width:1200px;text-align:center;top:102px">OUR SERVICES</h2>
  <div class="rule" style="left:564px;top:153px"></div>
  <svg class="arrow" style="left:42px;top:100px;top:300px" width="26" height="50" viewBox="0 0 26 50"><path d="M24 2 2 25l22 23" fill="none" stroke="#222" stroke-width="2"/></svg>
  <svg class="arrow" style="left:1132px;top:300px" width="26" height="50" viewBox="0 0 26 50"><path d="M2 2l22 23L2 48" fill="none" stroke="#222" stroke-width="2"/></svg>
  <div class="svc" style="left:108px"><div class="ring"><div class="pic" style="background:linear-gradient(150deg,#1c2226,#3a3a34 60%,#6b5a3a)" role="img" aria-label="Lit deck and patio at night"></div></div><h3>Lorem ipsum dolor</h3></div>
  <div class="svc" style="left:448px"><div class="ring"><div class="pic" style="background:linear-gradient(150deg,#3f6a2a,#9aa090 50%,#5a8a2f)" role="img" aria-label="Garden bed with pebbles and path lights"></div></div><h3>Lorem ipsum dolor</h3></div>
  <div class="svc" style="left:788px"><div class="ring"><div class="pic" style="background:linear-gradient(160deg,#3a4a3a,#4fa8d0 50%,#c9cfc4)" role="img" aria-label="Illuminated poolside landscaping"></div></div><h3>Lorem ipsum dolor</h3></div>
</section>

<!-- Offer -->
<div class="photo" style="left:0;top:2224px;width:614px;height:520px;background:linear-gradient(180deg,#6a7a86 0%,#4a5440 40%,#8a5a30 65%,#4a5a28 100%)" role="img" aria-label="Brick house lit at twilight"></div>
<div class="abs" style="left:1020px;top:2569px;width:94px;height:87px;background:var(--gold)"></div>
<div class="abs offer-box">
  We provide free estimates<br>and we are offering a
  <div class="big">10% Discount</div>
  to military, veterans, and<br>first responders
</div>

<!-- Demo kit -->
<h2 class="abs heading" style="left:110px;top:2860px">USE OUR DEMO KIT</h2>
<div class="rule" style="left:110px;top:2895px"></div>
<p class="abs about-text" style="left:110px;top:2933px;width:457px">we take pride in transforming outdoor spaces through innovative lighting solutions tailored to your vision. From landscape and holiday lighting to permanent installations, our effortless process and expert design deliver breathtaking results and lasting curb appeal. Backed by a lifetime warranty and quarterly service options, our commitment to quality and customer satisfaction is unwavering. Try before you buy and experience your home in a whole new light with our complimentary demo kit — see the stunning effects before you decide.</p>
<div class="btn" style="left:110px;top:3170px;width:152px;height:42px">Learn more <span class="dot"></span></div>
<div class="abs" style="left:783px;top:2844px;width:215px;height:388px;background:var(--gold)"></div>
<div class="photo" style="left:635px;top:2862px;width:453px;height:352px;background:linear-gradient(160deg,#1e2c44,#384a5a 40%,#7a6440 65%,#233018)" role="img" aria-label="Home facade with uplighting at night"></div>

<!-- Blog -->
<section class="abs blog">
  <h2 class="heading" style="position:absolute;left:0;width:1200px;text-align:center;top:110px">LATEST BLOG</h2>
  <div class="rule" style="left:564px;top:155px"></div>
  <svg class="arrow" style="left:42px;top:396px" width="26" height="50" viewBox="0 0 26 50"><path d="M24 2 2 25l22 23" fill="none" stroke="#222" stroke-width="2"/></svg>
  <svg class="arrow" style="left:1132px;top:396px" width="26" height="50" viewBox="0 0 26 50"><path d="M2 2l22 23L2 48" fill="none" stroke="#222" stroke-width="2"/></svg>
  <article class="card" style="left:111px"><div class="pic" style="background:linear-gradient(170deg,#1c2a48,#2a3550 55%,#6a5636)" role="img" aria-label="Two-storey home lit at night"></div><div class="body"><h4>Duis aute irure dolor in</h4><div class="date"><svg width="13" height="13" viewBox="0 0 13 13"><rect x="1" y="2" width="11" height="10" fill="none" stroke="var(--green)" stroke-width="1.5"/><path d="M1 5h11" stroke="var(--green)"/></svg>Jan 20, 2022</div><p>Lorem ipsum dolor sit amet, consect etur adipiscing elit, sed do eiusmod tempor incididunt ut labore</p></div></article>
  <article class="card" style="left:444px"><div class="pic" style="background:linear-gradient(170deg,#2a3a22,#4a4a2a 50%,#7a5a2a)" role="img" aria-label="Garden path lights among plants"></div><div class="body"><h4>Duis aute irure dolor in</h4><div class="date"><svg width="13" height="13" viewBox="0 0 13 13"><rect x="1" y="2" width="11" height="10" fill="none" stroke="var(--green)" stroke-width="1.5"/><path d="M1 5h11" stroke="var(--green)"/></svg>Jan 20, 2022</div><p>Lorem ipsum dolor sit amet, consect etur adipiscing elit, sed do eiusmod tempor incididunt ut labore</p></div></article>
  <article class="card" style="left:776px"><div class="pic" style="background:linear-gradient(170deg,#2a3a5a,#4a4a4a 55%,#6a5030)" role="img" aria-label="Modern stone house with exterior lighting"></div><div class="body"><h4>Duis aute irure dolor in</h4><div class="date"><svg width="13" height="13" viewBox="0 0 13 13"><rect x="1" y="2" width="11" height="10" fill="none" stroke="var(--green)" stroke-width="1.5"/><path d="M1 5h11" stroke="var(--green)"/></svg>Jan 20, 2022</div><p>Lorem ipsum dolor sit amet, consect etur adipiscing elit, sed do eiusmod tempor incididunt ut labore</p></div></article>
  <div class="btn" style="left:130px;top:558px;width:152px;height:42px">Learn more <span class="dot"></span></div>
  <div class="btn" style="left:462px;top:558px;width:152px;height:42px">Learn more <span class="dot"></span></div>
  <div class="btn" style="left:794px;top:558px;width:152px;height:42px">Learn more <span class="dot"></span></div>
</section>

<!-- Footer -->
<footer class="abs footer">
  <svg style="position:absolute;left:0;top:-30px" width="1200" height="110" viewBox="0 0 1200 110"><path d="M0 0H1200V30Q600 120 0 30Z" fill="var(--gold)"/><path d="M0 0H1200V24Q600 104 0 24Z" fill="var(--brick)"/></svg>
  <div style="position:absolute;left:110px;top:180px;display:flex;align-items:center;gap:10px;font-family:'Josefin Sans',sans-serif;font-weight:700;font-size:20px;line-height:1.05;width:190px"><span style="width:16px;height:16px;border-radius:50%;background:#fff;flex:none"></span>Corbin Lantern Lighting</div>
  <p style="position:absolute;left:110px;top:272px;width:275px;font-size:13px;line-height:21px">Lorem ipsum dolor sit amet, consectetur adipiscing elit, sed do eiusmod tempor incididunt ut labore et dolore Lorem ipsum dolor sit amet, consectetur adipiscing elit, sed do eiusmod tempor</p>
  <h5 style="left:437px">Contact us</h5>
  <div class="contact-item" style="top:240px"><svg width="14" height="18" viewBox="0 0 14 18" style="margin-top:4px"><path d="M7 0a7 7 0 017 7c0 5-7 11-7 11S0 12 0 7a7 7 0 017-7z" fill="var(--gold)"/><circle cx="7" cy="7" r="2.5" fill="var(--footer)"/></svg><span>Lorem ipsum dolor sit<br>nsectetur</span></div>
  <div class="contact-item" style="top:318px"><svg width="14" height="14" viewBox="0 0 24 24" style="margin-top:6px"><path fill="var(--gold)" d="M6.6 10.8a15 15 0 006.6 6.6l2.2-2.2c.3-.3.7-.4 1-.2 1.1.4 2.3.6 3.6.6.6 0 1 .4 1 1V20c0 .6-.4 1-1 1A17 17 0 013 4c0-.6.4-1 1-1h3.5c.6 0 1 .4 1 1 0 1.3.2 2.5.6 3.6.1.3 0 .7-.2 1z"/></svg><span>+1 888 888 8888</span></div>
  <div class="contact-item" style="top:370px"><svg width="15" height="12" viewBox="0 0 15 12" style="margin-top:7px"><rect width="15" height="12" fill="var(--gold)"/><path d="M0 0l7.5 6L15 0" fill="none" stroke="var(--footer)" stroke-width="1.5"/></svg><span>info@companyname.com</span></div>
  <h5 style="left:705px">Quick Links</h5>
  <ul class="flist" style="left:708px"><li>Home</li><li>About us</li><li>Services</li><li>Blog</li><li>Testimonials</li><li>Contact us</li></ul>
  <h5 style="left:912px">Information</h5>
  <ul class="flist" style="left:916px"><li>Privacy policy</li><li>Terms &amp; conditions</li><li>Faq</li><li>About us</li><li>Gallery</li><li>Project</li></ul>
</footer>
<div class="copy">© Copyrights 2025 Company name | All Rights reserved</div>

</body>
</html>
```